Neues Corporate Identity Web Design für einen coolen Energydrink
Zielgruppe
UPDATE: das BETA storyboard für das Video auf der neuen Seite.. jetzt in den Dateien, hier fehlt noch der sportliche dynamische abenteurliche part.. wird die tage erneut geupdatet..
Hallo Designer,
wir sind Velunora - ein junges Start-Up, die 'Guayusa - den Energydrink der Indianer' nach Deutschland gebracht haben. Mit unseren Produkten sprechen wir Backpacker / Abenteurer, Gesundheitsbewusste, Spirituelle, Kreative, Startups, Surfer, Skater, Weltverbesserer, Hipster und später auch Sportler und Gamer an. Und klaro auch die Energydrink und Kaffeejunkies ;-) ...
Aufgabenstellung
Neues Corporate Identity Design für eine Wordpress Seite mit Shop Funktion (Woocomerce)
Ihr findet eine PDF in den Dateien mit den genauen Wünschen von uns. -> BITTE LESEN!
Bilder könnt Ihr aus den bestehenden Auftritten entnehmen. Ihr findet diese auf unser Webseite: www.velunora.de auf unserem Facebook Account: www.facebook.com/Kolarintee/ auf unserem Instagram Account: www.instagram.com/velunora als auch auf unseren Produktseiten auf Kaufstadt. Weitere Bilder können aus bildervorrat-beispiel.de vorgeschlagen werden.
Die von uns verwendete Schriftart haben wir auch angehängt, ist aber kein Muss, wenn ihr andere Ideen habt, her damit!
Dateiübergabe in PSD Form, so das ein Webdesigner es gut umsetzen kann.

```html
<!DOCTYPE html>
<html lang="de">
<head>
<meta charset="utf-8">
<title>Velunora – Warum Guayusa?</title>
<link rel="stylesheet" href="https://fonts.googleapis.com/css2?family=Work+Sans:wght@400;500;700;800&display=swap">
<style>
  :root {
    --page-bg: #ffffff;
    --side-pattern: #f1f1ef;
    --ink: #3a3a3a;
    --ink-soft: #6a6a6a;
    --leaf-green: #8cc63f;
    --plantation-dark: #3f6b2a;
    --plantation-light: #9cc46a;
    --tea-light: #dfeccf;
    --tea-green: #9ccc4a;
    --band-tan: #e5bd95;
    --band-text: #ffffff;
    --band-strong: #7a4f2c;
  }
  * { box-sizing: border-box; margin: 0; padding: 0; }
  html, body { width: 1200px; height: 800px; overflow: hidden; }
  body {
    font-family: "Work Sans", Arial, sans-serif;
    background: var(--page-bg);
    color: var(--ink);
    position: relative;
  }
  .side-pattern {
    position: absolute;
    top: 130px;
    width: 150px;
    height: 470px;
    background: linear-gradient(180deg, var(--side-pattern), #f7f7f5);
  }
  .side-pattern--left { left: 0; }
  .side-pattern--right { right: 0; }
  .hero-photo {
    position: absolute;
    left: 0; top: 0;
    width: 1200px; height: 130px;
    background: linear-gradient(100deg, var(--plantation-dark) 0%, var(--plantation-light) 45%, #c8dca8 70%, var(--plantation-dark) 100%);
  }
  .intro-card {
    position: absolute;
    left: 150px; top: 60px;
    width: 900px; height: 540px;
    background: var(--page-bg);
  }
  .intro-card__title {
    position: absolute;
    top: 28px; left: 0; width: 100%;
    text-align: center;
    font-weight: 500;
    font-size: 44px;
    letter-spacing: 1px;
    color: var(--ink);
  }
  .intro-card__photo {
    position: absolute;
    left: 70px; top: 120px;
    width: 340px; height: 300px;
    border-radius: 46% 54% 50% 50%;
    background: radial-gradient(circle at 50% 45%, var(--tea-light) 0%, var(--tea-green) 55%, rgba(255,255,255,0) 72%);
  }
  .benefit-list {
    position: absolute;
    left: 490px; top: 130px;
    list-style: none;
  }
  .benefit-list__item {
    display: flex;
    align-items: flex-start;
    gap: 12px;
    margin-bottom: 26px;
    font-size: 25px;
    line-height: 1.2;
    color: var(--ink);
  }
  .benefit-list__item strong { font-weight: 800; }
  .benefit-list__icon { flex: 0 0 20px; margin-top: 6px; }
  .intro-card__button {
    position: absolute;
    left: 375px; top: 445px;
    width: 150px; height: 32px;
    border: 1.5px solid var(--ink-soft);
    background: var(--page-bg);
    font-family: inherit;
    font-size: 13px;
    font-weight: 500;
    letter-spacing: 0.5px;
    color: var(--ink);
  }
  .story-band {
    position: absolute;
    left: 0; top: 600px;
    width: 1200px; height: 200px;
    background: var(--band-tan);
  }
  .story-band__text {
    position: absolute;
    left: 150px; top: 52px;
    width: 650px;
    font-size: 19px;
    line-height: 1.55;
    color: var(--band-text);
  }
  .story-band__text strong { font-weight: 700; }
  .brand-mark {
    position: absolute;
    left: 880px; top: 20px;
    display: flex;
    flex-direction: column;
    align-items: center;
    gap: 10px;
  }
  .brand-mark__circle {
    width: 110px; height: 110px;
    border: 3px solid var(--band-text);
    border-radius: 50%;
  }
  .brand-mark__name {
    font-size: 20px;
    font-weight: 500;
    color: var(--band-text);
  }
</style>
</head>
<body>
  <div class="hero-photo" role="img" aria-label="Foto einer grünen Teeplantage an einem Hang"></div>
  <div class="side-pattern side-pattern--left" role="img" aria-label="Dezentes Ornamentmuster im Andenstil"></div>
  <div class="side-pattern side-pattern--right" role="img" aria-label="Dezentes Ornamentmuster im Andenstil"></div>

  <section class="intro-card">
    <h1 class="intro-card__title">WARUM GUAYUSA?</h1>
    <div class="intro-card__photo" role="img" aria-label="Glas mit grünem Guayusa-Tee und frischen Blättern"></div>
    <ul class="benefit-list">
      <li class="benefit-list__item">
        <svg class="benefit-list__icon" width="20" height="22" viewBox="0 0 20 22" aria-hidden="true"><path d="M3 20 C2 10 8 3 18 2 C18 12 12 19 3 20 Z" fill="var(--leaf-green)"/></svg>
        <span>100% <strong>handmade</strong> by<br>Quechua Indianern</span>
      </li>
      <li class="benefit-list__item">
        <svg class="benefit-list__icon" width="20" height="22" viewBox="0 0 20 22" aria-hidden="true"><path d="M3 20 C2 10 8 3 18 2 C18 12 12 19 3 20 Z" fill="var(--leaf-green)"/></svg>
        <span>mehr <strong>Koffein</strong> als Kaffe</span>
      </li>
      <li class="benefit-list__item">
        <svg class="benefit-list__icon" width="20" height="22" viewBox="0 0 20 22" aria-hidden="true"><path d="M3 20 C2 10 8 3 18 2 C18 12 12 19 3 20 Z" fill="var(--leaf-green)"/></svg>
        <span>leistung ausdauer<br>&amp; <strong>konzentration</strong></span>
      </li>
    </ul>
    <button class="intro-card__button" type="button">WARUM GUAYUSA?</button>
  </section>

  <section class="story-band">
    <p class="story-band__text"><strong>Velunora</strong> bedeutet in der Quechua Sprache „<strong>Andere Welt</strong>“. Das Logo ist eine Figur mit scheinbar nur einem Auge, denn das andere ist geschlossen, da der Schamane „Velunora“ in die andere Welt blickt und dort neue Kraft für den Tag sammelt.</p>
    <div class="brand-mark">
      <span class="brand-mark__circle" aria-hidden="true"></span>
      <span class="brand-mark__name">Velunora</span>
    </div>
  </section>
</body>
</html>
```